Brivora Collective Business Card Design

We need a business card design for Brivora Collective. We are a healthcare recruiting, wellness and education company. We partner with medical facilities to find quality candidates. We also offer free wellness courses.
The final design should communicate an emphasis on recruiting and wellness
The main purpose of the business card is to utilized it for networking events, give to hospitals, executives, VCs surgery centers and clinics. I want it to be sleek, clean, use of our brand colors and professional.

```html
<!DOCTYPE html>
<html lang="en">
<head>
<meta charset="utf-8">
<title>Brivora Collective Business Card</title>
<link rel="stylesheet" href="https://fonts.googleapis.com/css2?family=Montserrat:wght@300;400;500;600&display=swap">
<style>
  :root {
    --teal-deep: #055d55;
    --teal-mid: #0a6e64;
    --teal-bright: #0f8176;
    --brand-teal: #1f6e68;
    --paper: #ffffff;
    --backdrop: #e9ebea;
    --text-light: #f2f7f6;
  }
  * { margin: 0; padding: 0; box-sizing: border-box; }
  html, body { width: 1200px; height: 1014px; overflow: hidden; }
  body {
    background: var(--backdrop);
    font-family: "Montserrat", sans-serif;
    position: relative;
  }
  .card {
    position: absolute;
    top: 167px;
    width: 400px;
    height: 680px;
    border-radius: 34px;
    overflow: hidden;
    box-shadow: 0 10px 30px rgba(0,0,0,0.12);
  }
  .card-front {
    left: 160px;
    background: linear-gradient(160deg, var(--teal-mid) 0%, var(--teal-deep) 70%);
    color: var(--text-light);
  }
  .card-back {
    left: 640px;
    background: var(--paper);
    display: flex;
    align-items: center;
    justify-content: center;
  }
  .accent-square {
    position: absolute;
    top: 120px;
    left: 150px;
    width: 160px;
    height: 150px;
    border-radius: 28px;
    background: var(--teal-bright);
    opacity: 0.55;
  }
  .contact-block {
    position: absolute;
    left: 42px;
    top: 400px;
  }
  .person-name {
    font-size: 27px;
    font-weight: 600;
    letter-spacing: 1.5px;
  }
  .person-title {
    margin-top: 6px;
    font-size: 19px;
    font-weight: 300;
    letter-spacing: 1.5px;
  }
  .divider {
    width: 90px;
    height: 2px;
    background: var(--text-light);
    margin: 22px 0 24px;
  }
  .contact-line {
    font-size: 15px;
    font-weight: 300;
    letter-spacing: 1.2px;
    line-height: 1.75;
  }
  .brand-lockup {
    display: flex;
    align-items: center;
    gap: 14px;
  }
  .brand-square {
    width: 26px;
    height: 26px;
    border-radius: 5px;
    background: var(--brand-teal);
  }
  .brand-name {
    font-size: 30px;
    font-weight: 500;
    color: var(--brand-teal);
    letter-spacing: 0.5px;
    line-height: 1.1;
  }
</style>
</head>
<body>
  <section class="card card-front" aria-label="Card front">
    <div class="accent-square"></div>
    <div class="contact-block">
      <p class="person-name">Mara Quinlan</p>
      <p class="person-title">Co-Founder + CEO</p>
      <div class="divider"></div>
      <p class="contact-line">555.014.2290</p>
      <p class="contact-line">mara@brivoracollective.com</p>
      <p class="contact-line">www.brivoracollective.com</p>
    </div>
  </section>

  <section class="card card-back" aria-label="Card back">
    <div class="brand-lockup">
      <span class="brand-square"></span>
      <span class="brand-name">Brivora Collective</span>
    </div>
  </section>
</body>
</html>
```